Harrow Glen Kentucky Bourbon Whiskey

We need a label design for a bottle of whiskey. It is for a 750 ml bottle and needs to have a place to write in proof, age, and bottle number at bottom of label. It is a single barrel bourbon. We want to include our tree logo attached in the upload files in some way. Leave out the Distillery part to where it just says Harrow Glen Bourbon Whiskey with the tree. We need the label to be clean and modern. I have also attached a picture of the bottle the label is intended to go on.

Industry/Entity Type

Bourbon

Requirements
Must have
• Harrow Glen tree from file

```html
<!DOCTYPE html>
<html lang="en">
<head>
<meta charset="utf-8">
<title>Harrow Glen Kentucky Bourbon Whiskey – Label</title>
<link href="https://fonts.googleapis.com/css2?family=Cinzel:wght@400;600&family=Smokum&display=swap" rel="stylesheet">
<style>
  :root {
    --page: #d6d6d6;
    --label-black: #0e0e0e;
    --gold-deep: #a97a22;
    --gold: #d6a43c;
    --gold-light: #f0d68a;
    --ink: #161616;
    --paper: #ffffff;
    --cream: #f4f1ea;
  }
  html, body {
    margin: 0;
    padding: 0;
    width: 1124px;
    height: 1200px;
    overflow: hidden;
    background: var(--page);
  }
  .label {
    display: block;
    width: 1124px;
    height: 1200px;
  }
  .brand-name {
    font-family: "Cinzel", serif;
    font-weight: 600;
    font-size: 64px;
    fill: var(--cream);
    letter-spacing: 1px;
  }
  .product-title {
    font-family: "Smokum", cursive;
    font-size: 150px;
  }
  .subtitle {
    font-family: "Cinzel", serif;
    font-weight: 400;
    font-size: 30px;
    fill: var(--cream);
    letter-spacing: 1px;
  }
  .spirit-type {
    font-family: "Cinzel", serif;
    font-weight: 400;
    font-size: 62px;
    letter-spacing: 2px;
  }
  .volume {
    font-family: "Cinzel", serif;
    font-weight: 400;
    font-size: 60px;
    fill: var(--gold);
  }
  .field-label {
    font-family: "Cinzel", serif;
    font-weight: 400;
    font-size: 16px;
    fill: var(--ink);
    letter-spacing: 0.5px;
  }
  .rule-dark { stroke: var(--ink); stroke-width: 2; }
  .rule-light { stroke: var(--cream); stroke-width: 2; }
</style>
</head>
<body>
<svg class="label" viewBox="0 0 1124 1200" xmlns="http://www.w3.org/2000/svg" aria-label="Harrow Glen Kentucky Bourbon Whiskey bottle label">
  <defs>
    <linearGradient id="gold-band" x1="0" y1="0" x2="1" y2="0">
      <stop offset="0" stop-color="var(--gold-deep)"/>
      <stop offset="0.35" stop-color="var(--gold)"/>
      <stop offset="0.6" stop-color="#e8b94a"/>
      <stop offset="0.85" stop-color="var(--gold-light)"/>
      <stop offset="1" stop-color="var(--gold-deep)"/>
    </linearGradient>
    <linearGradient id="gold-type" x1="0" y1="0" x2="0" y2="1">
      <stop offset="0" stop-color="var(--gold-light)"/>
      <stop offset="0.5" stop-color="var(--gold)"/>
      <stop offset="1" stop-color="var(--gold-deep)"/>
    </linearGradient>
    <pattern id="ticket-notches" x="128" y="0" width="17" height="10" patternUnits="userSpaceOnUse">
      <rect x="9" y="0" width="8" height="10" fill="var(--label-black)"/>
    </pattern>
    <filter id="type-shadow" x="-5%" y="-10%" width="110%" height="130%">
      <feDropShadow dx="2" dy="4" stdDeviation="3" flood-color="#000" flood-opacity="0.8"/>
    </filter>
  </defs>

  <!-- label body -->
  <rect class="label-body" x="0" y="41" width="1124" height="1115" fill="var(--label-black)"/>

  <!-- top band -->
  <rect class="band-top" x="0" y="71" width="1124" height="21" fill="url(#gold-band)"/>

  <!-- brand -->
  <circle class="brand-dot" cx="562" cy="290" r="14" fill="var(--gold)"/>
  <text class="brand-name" x="562" y="396" text-anchor="middle">HARROW GLEN</text>

  <!-- product title -->
  <text class="product-title" x="112" y="622" textLength="898" lengthAdjust="spacingAndGlyphs" fill="url(#gold-type)" filter="url(#type-shadow)">KENTUCKY BOURBON</text>

  <!-- divider with dot -->
  <line class="rule-light" x1="115" y1="641" x2="540" y2="641"/>
  <circle cx="562" cy="641" r="6" fill="var(--cream)"/>
  <line class="rule-light" x1="584" y1="641" x2="1007" y2="641"/>

  <text class="subtitle" x="562" y="698" text-anchor="middle">ORIGINAL</text>
  <text class="spirit-type" x="562" y="754" text-anchor="middle" fill="url(#gold-type)" filter="url(#type-shadow)">WHISKEY</text>

  <!-- write-in ticket -->
  <g class="ticket">
    <rect x="128" y="797" width="862" height="237" fill="var(--paper)"/>
    <rect x="128" y="797" width="862" height="10" fill="url(#ticket-notches)"/>
    <rect x="128" y="1024" width="862" height="10" fill="url(#ticket-notches)"/>

    <line class="rule-dark" x1="152" y1="842" x2="969" y2="842"/>
    <text class="volume" x="150" y="904">750 ML</text>
    <line class="rule-dark" x1="400" y1="854" x2="400" y2="909"/>
    <text class="field-label" x="416" y="868">AGE</text>
    <line class="rule-dark" x1="574" y1="854" x2="574" y2="909"/>
    <text class="field-label" x="593" y="868">BOTTLE NO.</text>
    <line class="rule-dark" x1="152" y1="919" x2="969" y2="919"/>
    <text class="field-label" x="154" y="943">PROOF</text>
    <line class="rule-dark" x1="152" y1="997" x2="969" y2="997"/>
  </g>

  <!-- bottom band -->
  <rect class="band-bottom" x="0" y="1073" width="1124" height="48" fill="url(#gold-band)"/>
</svg>
</body>
</html>
```